Meadow Paw Web Site

We have basically a start up business that I need help with. This project is just for the web site.

Our product is a frozen raw pet food that promotes weight control, less shedding, smaller stools and an overall better health. The product is in nugget form similar to what you would see in a steak shish kabob. I only share that with you in case you want to incorporate that in the design.

We have been in business for 17 years but all of our sales have been word of mouth. We are going to be launching an infomercial this summer and I need everything stated previously to be completed before we can launch the infomercial.

We need the following (6) pages:

Home:
This is where we need to have the ability to purchase our products. Our main goal is to get the consumer to purchase our product. We have our own shopping cart so we just need to allow for the insertion of that shopping cart.

Why Raw:
This will just be a page with 4-5 paragraphs and an embedded YouTube video.

How to Use:
We will need a page with a chart (4 Columns wide with 6 rows) as well as an embedded YouTube video.

Customer Success Stories:
Allow us to add these as we move forward. I need a placeholder for an image of the customers pet and a paragraph or two explaining the situation

Where to Buy:
- Online - Find a Retailer - Find a Local Distributor - Call to Order

Contact Us:
Lantern Creek Companies, Inc.
2740 Lantern Cr
Eagan, MN 55122
(800) 555-0142

We need to provide links to our to be created... Facebook page, Twitter Account, Youtube Channel, Google circle, Blog
Updates

All, I have received many front page designs that look good.  Please notice in the brief that I need multiple pages built not just the home page.  

Thanks,

Dale

Reason: I need to see the rest of the pages. Thanks, Dale

Target Market(s)

Women between the ages of 30 & 60.

Industry/Entity Type

Shopping

```html
<!DOCTYPE html>
<html lang="en">
<head>
<meta charset="utf-8">
<title>Meadow Paw – How to Use</title>
<link rel="stylesheet" href="https://fonts.googleapis.com/css2?family=Open+Sans:wght@400;600;700;800&display=swap">
<style>
:root{
  --orange:#d9481e;
  --orange-dark:#b8370f;
  --orange-light:#ef6a2c;
  --yellow:#f6d31b;
  --page:#f1f1f1;
  --panel:#ffffff;
  --ink:#333333;
  --muted:#777777;
  --line:#dddddd;
  --footer:#2f2f2f;
  --footer-dark:#232323;
  --footer-text:#bdbdbd;
  --logo-bg:#1e1a17;
}
*{box-sizing:border-box;margin:0;padding:0}
html,body{width:880px;height:1200px;overflow:hidden}
body{background:var(--page);font-family:"Open Sans",Arial,sans-serif;color:var(--ink);position:relative}
.page{width:880px;height:1200px;position:relative}

/* header */
.site-header{position:absolute;left:0;top:0;width:880px;height:120px}
.brand{position:absolute;left:88px;top:10px;width:120px;height:62px;background:var(--logo-bg);border-radius:6px;display:flex;align-items:center;justify-content:center;gap:7px;box-shadow:0 2px 4px rgba(0,0,0,.25)}
.brand-dot{width:12px;height:12px;border-radius:50%;background:var(--orange-light)}
.brand-name{color:#fff;font-weight:700;font-size:15px}
.account-links{position:absolute;right:88px;top:12px;font-size:8px;color:var(--muted);letter-spacing:.3px}
.account-links span{margin:0 4px}
.auth{position:absolute;right:88px;top:42px;display:flex;gap:8px}
.btn{font-size:9px;font-weight:600;padding:3px 12px;border-radius:3px}
.btn-sign{background:var(--orange);color:#fff}
.btn-register{background:var(--yellow);color:#333}
.cart{position:absolute;left:528px;top:86px;display:flex;align-items:center;gap:6px;font-size:8px;font-weight:700;color:var(--orange)}
.cart .count{color:var(--muted);font-weight:600;margin-left:6px}
.search{position:absolute;right:88px;top:82px;width:90px;height:18px;border:1px solid var(--line);border-radius:9px;background:#fff;font-size:8px;color:#aaa;padding:3px 10px}
.search svg{position:absolute;right:6px;top:3px}

.main-nav{position:absolute;left:88px;top:120px;width:704px;height:30px;background:linear-gradient(var(--orange-light),var(--orange));border-radius:4px;display:flex;align-items:center}
.main-nav a{flex:1;text-align:center;color:#fff;font-size:11px;font-weight:700;text-decoration:none;border-left:1px solid rgba(255,255,255,.35);line-height:30px}
.main-nav a.home{flex:0 0 60px;border-left:none;display:flex;align-items:center;justify-content:center}

/* content */
.page-title{position:absolute;left:88px;top:186px;font-size:16px;font-weight:800;color:var(--ink);letter-spacing:.3px}
.page-title b{color:var(--orange)}
.title-rule{position:absolute;left:88px;top:212px;width:704px;height:2px;background:var(--line)}
.title-rule::before{content:"";position:absolute;left:0;top:0;width:50px;height:2px;background:var(--orange)}

.chart-panel{position:absolute;left:88px;top:232px;width:704px;height:370px;background:var(--panel);border:1px solid var(--line)}
.chart-panel svg{display:block}

.video{position:absolute;left:88px;top:640px;width:704px;height:328px;border:5px solid #fff;box-shadow:0 1px 4px rgba(0,0,0,.2);background:linear-gradient(180deg,#5a8a2e 0%,#c89a4e 45%,#e2b56a 70%,#8fae4a 100%)}
.play{position:absolute;left:50%;top:50%;width:50px;height:50px;margin:-25px 0 0 -25px;border-radius:50%;background:rgba(0,0,0,.55);border:2px solid #fff}
.play::after{content:"";position:absolute;left:19px;top:14px;border-left:16px solid #fff;border-top:10px solid transparent;border-bottom:10px solid transparent}

/* footer */
.site-footer{position:absolute;left:0;top:985px;width:880px;height:187px;background:var(--footer);color:var(--footer-text)}
.footer-col{position:absolute;top:18px;font-size:8px;line-height:13px}
.footer-col h4{color:#fff;font-size:11px;font-weight:700;margin-bottom:8px}
.footer-col p{margin:0}
.col-links{left:88px}
.col-products{left:200px}
.col-buy{left:312px}
.col-contact{left:448px}
.col-news{left:640px;width:152px}
.contact-phone{display:flex;align-items:center;gap:5px;margin-top:6px}
.news-input{margin-top:10px;height:18px;background:#fff;border-radius:2px;width:100%}
.subscribe{margin-top:6px;margin-left:auto;width:58px;height:16px;background:var(--orange);color:#fff;font-size:8px;text-align:center;line-height:16px;border-radius:2px}
.social{display:flex;gap:4px;margin-top:8px}
.social span{width:16px;height:16px;border-radius:2px;background:#3b5998}
.social span:nth-child(2){background:#41a9e0}
.social span:nth-child(3){background:#d24a3a}
.social span:nth-child(4){background:#c4302b}
.social span:nth-child(5){background:#f28b2c}
.footer-bottom{position:absolute;left:0;top:1172px;width:880px;height:28px;background:var(--footer-dark);font-size:8px;color:#8d8d8d}
.footer-bottom .copy{position:absolute;left:88px;top:9px}
.footer-bottom .credit{position:absolute;right:88px;top:9px}
</style>
</head>
<body>
<div class="page">
  <header class="site-header">
    <div class="brand"><span class="brand-dot"></span><span class="brand-name">Meadow Paw</span></div>
    <div class="account-links">MY ACCOUNT<span>|</span>WISH LIST<span>|</span>MY CART<span>|</span>CHECKOUT</div>
    <div class="auth"><span class="btn btn-sign">Sign in</span><span class="btn btn-register">Register</span></div>
    <div class="cart">
      <svg width="14" height="12" viewBox="0 0 14 12"><path d="M0 1h3l2 7h7l2-5H4" fill="none" stroke="#d9481e" stroke-width="1.5"/><circle cx="6" cy="10.5" r="1.2" fill="#d9481e"/><circle cx="11" cy="10.5" r="1.2" fill="#d9481e"/></svg>
      SHOPPING CART <span class="count">(0) ITEMS</span>
    </div>
    <div class="search">Search...
      <svg width="10" height="10" viewBox="0 0 10 10"><circle cx="4" cy="4" r="3" fill="none" stroke="#d9481e" stroke-width="1.4"/><path d="M6.3 6.3L9 9" stroke="#d9481e" stroke-width="1.4"/></svg>
    </div>
    <nav class="main-nav">
      <a class="home" href="#" aria-label="Home"><svg width="14" height="12" viewBox="0 0 14 12"><path d="M7 0L0 6h2v6h4V8h2v4h4V6h2z" fill="#fff"/></svg></a>
      <a href="#">Why Raw</a>
      <a href="#">How to Use</a>
      <a href="#">Where to Buy</a>
      <a href="#">Success Stories</a>
      <a href="#">Contact Us</a>
    </nav>
  </header>

  <main>
    <h1 class="page-title">HOW <b>TO USE</b></h1>
    <div class="title-rule"></div>

    <section class="chart-panel">
      <svg width="702" height="368" viewBox="0 0 702 368" font-family="Open Sans, Arial, sans-serif">
        <g stroke="#e2e2e2" stroke-width="1">
          <line x1="55" y1="40" x2="680" y2="40"/>
          <line x1="55" y1="98" x2="680" y2="98"/>
          <line x1="55" y1="156" x2="680" y2="156"/>
          <line x1="55" y1="214" x2="680" y2="214"/>
          <line x1="55" y1="272" x2="680" y2="272"/>
        </g>
        <line x1="55" y1="330" x2="680" y2="330" stroke="#999" stroke-width="1"/>
        <g font-size="12" fill="#444" text-anchor="end">
          <text x="40" y="44">125</text>
          <text x="40" y="102">100</text>
          <text x="40" y="160">75</text>
          <text x="40" y="218">50</text>
          <text x="40" y="276">25</text>
          <text x="40" y="334">0</text>
        </g>
        <g fill="#c9401a">
          <rect x="140" y="168" width="50" height="162"/>
          <rect x="256" y="79" width="50" height="251"/>
          <rect x="368" y="96" width="50" height="234"/>
          <rect x="490" y="126" width="50" height="204"/>
        </g>
        <g fill="#fff" font-size="15" text-anchor="middle">
          <text transform="translate(170 205) rotate(-90)">56%</text>
          <text transform="translate(286 116) rotate(-90)">108%</text>
          <text transform="translate(398 133) rotate(-90)">96%</text>
          <text transform="translate(520 163) rotate(-90)">82%</text>
        </g>
      </svg>
    </section>

    <section class="video" role="img" aria-label="Video still of three golden retriever puppies with a play button">
      <span class="play"></span>
    </section>
  </main>

  <footer class="site-footer">
    <div class="footer-col col-links">
      <h4>Quick Links</h4>
      <p>Why Raw</p><p>How to Use</p><p>Where to Buy</p><p>Success Stories</p><p>How to Order</p><p>How to Buy</p><p>Contact Us</p>
    </div>
    <div class="footer-col col-products">
      <h4>Top Products</h4>
      <p>Product 1</p><p>Product 2</p><p>Product 3</p><p>Product 4</p><p>Product 5</p><p>Product 6</p>
    </div>
    <div class="footer-col col-buy">
      <h4>Where to Buy</h4>
      <p>Find a Retailer</p><p>Find a Local Distributor</p><p>Call to Order</p>
    </div>
    <div class="footer-col col-contact">
      <h4>Contact Information</h4>
      <p>Lantern Creek Companies, Inc.</p><p>2740 Lantern Cr</p><p>Eagan, MN 55122</p>
      <p class="contact-phone"><svg width="9" height="9" viewBox="0 0 10 10"><path d="M2 0l2 2-1 2 3 3 2-1 2 2-2 2C4 10 0 6 0 2z" fill="#bdbdbd"/></svg>+1 (800) 555-0142</p>
    </div>
    <div class="footer-col col-news">
      <h4>Newsletter</h4>
      <p>Connect with a handful of health and wellness directions</p>
      <div class="news-input"></div>
      <div class="subscribe">Subscribe</div>
      <div class="social"><span></span><span></span><span></span><span></span><span></span></div>
    </div>
  </footer>
  <div class="footer-bottom">
    <span class="copy">Copyright Meadow Paw © 2014. Privacy Policy</span>
    <span class="credit">Designed &amp; Developed by Northgate Studio</span>
  </div>
</div>
</body>
</html>
```